Tailbrook Website Design

Need a website for a Dog Grooiming business. Please make it simular to these:

https://www.furvanto.com
https://haulnorix.com
https://meadowpetrin.com
https://www.drivelumo.com/search/

```html
<!DOCTYPE html>
<html lang="en">
<head>
<meta charset="utf-8">
<title>Tailbrook — Doorstep Dog Grooming</title>
<link rel="stylesheet" href="https://fonts.googleapis.com/css2?family=Arimo:wght@400;700&display=swap">
<style>
:root{
  --teal:#12d3a0;
  --aqua:#16b6c9;
  --blue:#1a86f2;
  --white:#ffffff;
  --ink:#111111;
  --body:#444444;
  --green:#2ebd6e;
  --star:#f4b400;
  --footer:#1f1f1f;
  --footer-line:#3a3a3a;
}
*{box-sizing:border-box;margin:0;padding:0}
html,body{width:1200px;height:4141px;overflow:hidden}
body{position:relative;font-family:"Arimo",Arial,sans-serif;color:var(--ink);background:var(--white)}
.abs{position:absolute}
a{color:inherit;text-decoration:none}

/* hero */
.hero{left:0;top:0;width:1200px;height:1623px;
  background:linear-gradient(200deg,var(--teal) 0%,var(--aqua) 30%,#1a9ef0 60%,var(--blue) 100%)}
.logo{left:100px;top:18px;font-size:34px;font-weight:700;color:var(--white)}
.nav{font-size:15px;font-weight:700;color:var(--white)}
.nav a{position:absolute;white-space:nowrap}
.btn-outline{border:2px solid var(--white);border-radius:22px;color:var(--white);font-weight:700;
  display:flex;align-items:center;justify-content:center;gap:8px;font-size:16px}
.btn-solid{background:var(--white);border-radius:22px;color:var(--blue);font-weight:700;
  display:flex;align-items:center;justify-content:center;gap:6px;font-size:15px}
.hero-title{left:97px;top:196px;font-size:60px;line-height:52px;font-weight:700;color:var(--white)}
.hero-sub{left:100px;top:320px;font-size:22px;line-height:27px;font-weight:700;color:var(--white)}
.photo{background:linear-gradient(160deg,#8aa89a,#5d7f6d)}
.sig-title{left:653px;top:806px;font-size:55px;line-height:53px;font-weight:700;color:var(--white);white-space:nowrap}
.sig-sub{left:653px;top:928px;font-size:22px;line-height:27px;font-weight:700;color:var(--white)}
.sig-phone{left:653px;top:1001px;font-size:20px;color:var(--white)}
.sig-phone u{text-underline-offset:3px}

/* services */
.svc-icon{width:92px;height:92px;border-radius:50%;background:var(--white);
  box-shadow:0 0 0 8px rgba(255,255,255,.3);display:flex;align-items:center;justify-content:center}
.svc-label{font-size:22px;line-height:30px;font-weight:700;color:var(--white)}
.svc-label.right{text-align:right}

/* testimonials */
.section-title{width:1200px;left:0;text-align:center;font-size:36px;font-weight:700}
.card{width:319px;height:244px;background:var(--white);box-shadow:0 2px 10px rgba(0,0,0,.12);padding:18px 20px}
.card .who{display:flex;align-items:center;gap:12px}
.avatar{width:58px;height:58px;border-radius:50%;background:linear-gradient(#d8c2b0,#9c7d66);flex:none}
.name{font-size:15px;font-weight:700}
.meta{font-size:12px;color:#777;margin-top:3px}
.meta span{color:var(--star);letter-spacing:1px}
.quote{font-size:14px;line-height:30px;color:var(--body);margin-top:10px}
.more{font-size:14px;font-weight:700;color:var(--green)}

/* cta */
.cta{left:0;top:2643px;width:1200px;height:373px;
  background:linear-gradient(100deg,#1a8cf0 0%,#19a9d7 45%,var(--teal) 100%)}
.cta-title{width:1200px;left:0;top:2728px;text-align:center;color:var(--white);font-size:38px;font-weight:700}
.cta-text{width:1200px;left:0;top:2799px;text-align:center;color:var(--white);font-size:14px;line-height:29px}

/* gallery */
.tile{width:235px;height:232px}

/* footer */
.footer{left:0;top:3749px;width:1200px;height:392px;background:var(--footer);color:var(--white)}
.f-head{font-size:22px;font-weight:700}
.f-list{list-style:none;font-size:15px;line-height:32px}
.f-contact{font-size:15px;line-height:20px;display:flex;gap:14px;align-items:center}
.f-ico{width:38px;height:38px;border-radius:50%;background:#333;display:flex;align-items:center;justify-content:center;flex:none}
.social{width:38px;height:38px;border-radius:50%;background:#333;display:flex;align-items:center;justify-content:center}
.social i{display:block;width:12px;height:12px;border-radius:50%;background:var(--white)}
.email{left:772px;top:3922px;width:270px;height:44px;background:var(--white);color:#333;font-size:14px;padding:14px 14px}
.send{left:1051px;top:3922px;width:49px;height:44px;background:#1ba3e0;display:flex;align-items:center;justify-content:center}
.rule{left:101px;top:4056px;width:999px;height:1px;background:var(--footer-line)}
.copy{left:0;width:1200px;top:4082px;text-align:center;font-size:15px}
</style>
</head>
<body>

<section class="hero abs">
  <div class="logo abs">Tailbrook</div>
  <nav class="nav abs" style="left:0;top:30px;width:1200px;height:20px">
    <a style="left:399px">Locations</a>
    <a style="left:506px">Careers</a>
    <a style="left:600px">About</a>
    <a style="left:680px">Blog</a>
    <a style="left:749px">FAQ</a>
    <a style="left:815px">(212) 555-0148</a>
  </nav>
  <a class="btn-outline abs" style="left:955px;top:22px;width:145px;height:38px">Book Online</a>

  <h1 class="hero-title abs">Doorstep<br>Dog Grooming</h1>
  <p class="hero-sub abs">Sed ut perspiciatis unde omnis iste<br>natus error sit voluptatem</p>
  <a class="btn-solid abs" style="left:100px;top:394px;width:162px;height:38px">Book Online
    <svg width="14" height="12" viewBox="0 0 14 12"><path d="M1 6h11M8 2l4 4-4 4" stroke="currentColor" stroke-width="1.8" fill="none"/></svg></a>

  <div class="photo abs" role="img" aria-label="Suburban house with a branded grooming van parked in front"
       style="left:555px;top:64px;width:645px;height:580px;border-radius:0 0 0 260px;background:linear-gradient(170deg,#c9b79a 0%,#8fb07c 45%,#e9edf0 70%,#5a6a4f 100%)"></div>
  <div class="photo abs" role="img" aria-label="Golden retriever and pug sitting side by side"
       style="left:96px;top:514px;width:459px;height:636px;border-radius:46% 46% 20% 20%;background:linear-gradient(180deg,#e9d3b0 0%,#d7b78d 55%,#c8a67e 100%)"></div>

  <h2 class="sig-title abs">The Tailbrook<br>Signature Service</h2>
  <p class="sig-sub abs">Sed ut perspiciatis unde omnis iste<br>natus error sit voluptatem</p>
  <p class="sig-phone abs">(800) 555-0193 or <u>Book Online</u></p>
  <a class="btn-outline abs" style="left:653px;top:1050px;width:117px;height:38px">
    <svg width="20" height="16" viewBox="0 0 20 16"><path d="M2 2h11v8H6l-3 3v-3H2z" fill="#fff"/><path d="M15 5h3v8h-1v2l-2-2h-6v-2" fill="none" stroke="#fff" stroke-width="1.5"/></svg>Text</a>
  <a class="btn-outline abs" style="left:784px;top:1050px;width:118px;height:38px">
    <svg width="16" height="16" viewBox="0 0 24 24"><path d="M6.6 10.8a15.1 15.1 0 0 0 6.6 6.6l2.2-2.2a1 1 0 0 1 1-.25 11.4 11.4 0 0 0 3.6.57 1 1 0 0 1 1 1V20a1 1 0 0 1-1 1A17 17 0 0 1 3 4a1 1 0 0 1 1-1h3.5a1 1 0 0 1 1 1c0 1.25.2 2.45.57 3.57a1 1 0 0 1-.25 1z" fill="#fff"/></svg>Call</a>

  <!-- services arc -->
  <svg class="abs" style="left:0;top:1240px" width="1200" height="383" viewBox="0 0 1200 383">
    <path d="M283 383 Q300 190 455 59 Q600 -10 744 59 Q900 190 916 383" fill="none" stroke="var(--teal)" stroke-width="3"/>
    <circle cx="521" cy="69" r="7" fill="none" stroke="#fff" stroke-width="2.5"/>
    <circle cx="460" cy="156" r="14" fill="none" stroke="#fff" stroke-width="3"/>
    <circle cx="722" cy="138" r="11" fill="none" stroke="#fff" stroke-width="3"/>
  </svg>
  <div class="photo abs" role="img" aria-label="Two bulldog puppies in a wooden bath tub with shampoo bottles and towels"
       style="left:426px;top:1318px;width:314px;height:297px;border-radius:40% 40% 10% 10%;background:linear-gradient(180deg,#d9c9b4 0%,#c39a63 65%,#efe8dc 100%)"></div>

  <div class="svc-icon abs" style="left:409px;top:1253px"><svg width="44" height="44" viewBox="0 0 44 44" fill="none" stroke="var(--blue)" stroke-width="2"><path d="M6 24h32v6a8 8 0 0 1-8 8H14a8 8 0 0 1-8-8z"/><path d="M12 38l-2 4M32 38l2 4"/><circle cx="22" cy="14" r="7"/></svg></div>
  <div class="svc-label right abs" style="left:180px;top:1271px;width:202px">Warm Filtered<br>Water Bath</div>

  <div class="svc-icon abs" style="left:698px;top:1253px"><svg width="44" height="44" viewBox="0 0 44 44" fill="none" stroke="var(--blue)" stroke-width="2"><path d="M6 10h22a8 8 0 0 1 0 16H6z"/><path d="M18 26l-3 14h8l3-14"/><path d="M34 14h6M34 22h6"/></svg></div>
  <div class="svc-label abs" style="left:806px;top:1271px;width:200px">Gentle Brush &amp;<br>Blowout</div>

  <div class="svc-icon abs" style="left:284px;top:1369px"><svg width="44" height="44" viewBox="0 0 44 44" fill="none" stroke="var(--blue)" stroke-width="2"><rect x="8" y="22" width="16" height="16" rx="2"/><rect x="26" y="10" width="12" height="28" rx="2"/><path d="M30 6h4v4h-4z"/></svg></div>
  <div class="svc-label right abs" style="left:100px;top:1386px;width:170px">All Natural<br>Products</div>

  <div class="svc-icon abs" style="left:822px;top:1369px"><svg width="44" height="44" viewBox="0 0 44 44" fill="none" stroke="var(--blue)" stroke-width="2"><path d="M16 4l2 18M28 4l-2 18"/><circle cx="16" cy="32" r="6"/><circle cx="28" cy="32" r="6"/></svg></div>
  <div class="svc-label abs" style="left:928px;top:1386px;width:140px">Trim &amp;<br>&nbsp;File Nails</div>

  <div class="svc-icon abs" style="left:237px;top:1502px"><svg width="44" height="44" viewBox="0 0 44 44" fill="none" stroke="var(--blue)" stroke-width="2"><rect x="8" y="6" width="14" height="16" rx="2"/><path d="M15 22v16M26 10l8 28M36 10l-8 28"/></svg></div>
  <div class="svc-label right abs" style="left:40px;top:1519px;width:182px">Breed Specific<br>Pro Groom</div>

  <div class="svc-icon abs" style="left:870px;top:1502px"><svg width="44" height="44" viewBox="0 0 44 44" fill="none" stroke="var(--blue)" stroke-width="2"><path d="M20 8l3 9 9 3-9 3-3 9-3-9-9-3 9-3z"/><path d="M34 28l1.5 4 4 1.5-4 1.5-1.5 4-1.5-4-4-1.5 4-1.5z"/></svg></div>
  <div class="svc-label abs" style="left:976px;top:1519px;width:190px">Clean Teeth &amp;<br>Ears</div>
</section>

<div class="photo abs" role="img" aria-label="Groomers brushing a chow chow and drying a small dog in a salon"
     style="left:0;top:1623px;width:1200px;height:541px;background:linear-gradient(90deg,#e7c7b6 0%,#c48a52 45%,#e2ddd8 75%,#bfb6ad 100%)"></div>
<div class="abs" style="left:563px;top:1845px;width:96px;height:96px;border-radius:50%;background:rgba(255,255,255,.55);display:flex;align-items:center;justify-content:center">
  <div style="width:76px;height:76px;border-radius:50%;background:#fff;display:flex;align-items:center;justify-content:center">
    <svg width="22" height="24" viewBox="0 0 22 24"><path d="M3 2l17 10L3 22z" fill="var(--blue)"/></svg></div></div>

<h2 class="section-title abs" style="top:2249px">Testimonials</h2>
<article class="card abs" style="left:100px;top:2314px">
  <div class="who"><div class="avatar" role="img" aria-label="Reviewer portrait"></div><div><div class="name">Jamie Rowan</div><div class="meta"><span>★★★★★</span> (2days ago)</div></div></div>
  <p class="quote">Lorem ipsum dolor sit amet, consectetur adipiscing elit, sed do ed ter incididunt ut labore et dolore magqua. Quis ipsum suspendisse ultrices gravida.</p>
  <p class="more">Read More...</p>
</article>
<article class="card abs" style="left:440px;top:2314px">
  <div class="who"><div class="avatar" role="img" aria-label="Reviewer portrait"></div><div><div class="name">Jamie Rowan</div><div class="meta"><span>★★★★★</span> (2days ago)</div></div></div>
  <p class="quote">Lorem ipsum dolor sit amet, consectetur adipiscing elit, sed do ed ter incididunt ut labore et dolore magqua. Quis ipsum suspendisse ultrices gravida.</p>
  <p class="more">Read More...</p>
</article>
<article class="card abs" style="left:781px;top:2314px">
  <div class="who"><div class="avatar" role="img" aria-label="Reviewer portrait"></div><div><div class="name">Jamie Rowan</div><div class="meta"><span>★★★★★</span> (2days ago)</div></div></div>
  <p class="quote">Lorem ipsum dolor sit amet, consectetur adipiscing elit, sed do ed ter incididunt ut labore et dolore magqua. Quis ipsum suspendisse ultrices gravida.</p>
  <p class="more">Read More...</p>
</article>

<section class="cta abs" role="img" aria-label="Faded photo of a dog being groomed behind a blue-to-green overlay"></section>
<h2 class="cta-title abs">Get Your Dog Grooiming Today.</h2>
<p class="cta-text abs">Lorem ipsum dolor sit amet, consectetur adipiscing elit, seiusmod tempor incididunt<br>ut labore et dolore magna aliqua. Quis ipsum pendisse</p>
<a class="btn-outline abs" style="left:526px;top:2876px;width:148px;height:38px;font-size:15px">Contact Us</a>

<h2 class="section-title abs" style="top:3104px">Follow On @Tailbrook</h2>
<div class="tile photo abs" role="img" aria-label="Poodle being groomed" style="left:109px;top:3170px;background:linear-gradient(150deg,#efe4da,#d2b7a0)"></div>
<div class="tile photo abs" role="img" aria-label="Pomeranian being brushed" style="left:358px;top:3170px;background:linear-gradient(150deg,#e6dfd6,#d19b5c)"></div>
<div class="tile photo abs" role="img" aria-label="Maltese with a red bow" style="left:608px;top:3170px;background:linear-gradient(150deg,#6b5c55,#efece8)"></div>
<div class="tile photo abs" role="img" aria-label="Retriever being showered" style="left:857px;top:3170px;background:linear-gradient(150deg,#7c8890,#d0a36e)"></div>
<div class="tile photo abs" role="img" aria-label="Terrier wrapped in a green towel" style="left:109px;top:3416px;background:linear-gradient(150deg,#f1efe9,#a9c44a)"></div>
<div class="tile photo abs" role="img" aria-label="Yorkshire terrier having its hair tied" style="left:358px;top:3416px;background:linear-gradient(150deg,#dcd6cf,#8c6a48)"></div>
<div class="tile photo abs" role="img" aria-label="Pug resting on a blanket" style="left:608px;top:3416px;background:linear-gradient(150deg,#b9ad9f,#e7d9c7)"></div>
<div class="tile photo abs" role="img" aria-label="Pomeranian being brushed on a table" style="left:857px;top:3416px;background:linear-gradient(150deg,#ece7e1,#cf9a5a)"></div>

<footer class="footer abs">
  <h3 class="f-head abs" style="left:101px;top:82px">Quick Links</h3>
  <ul class="f-list abs" style="left:101px;top:117px"><li>Locations</li><li>Careers</li><li>About</li><li>Blog</li><li>FAQ</li></ul>
  <h3 class="f-head abs" style="left:281px;top:82px">Other Links</h3>
  <ul class="f-list abs" style="left:281px;top:117px"><li>Privacy Policy</li><li>Terms of Service</li><li>Credit</li><li>FAQ</li></ul>
  <h3 class="f-head abs" style="left:464px;top:82px">Contact Us</h3>
  <div class="f-contact abs" style="left:464px;top:123px"><span class="f-ico"><svg width="16" height="20" viewBox="0 0 16 20"><path d="M8 0a8 8 0 0 1 8 8c0 6-8 12-8 12S0 14 0 8a8 8 0 0 1 8-8z" fill="#fff"/><circle cx="8" cy="8" r="3" fill="#333"/></svg></span><span>48 Larkfield Lane Brookvale<br>USA&nbsp; 20417</span></div>
  <div class="f-contact abs" style="left:464px;top:185px"><span class="f-ico"><svg width="16" height="16" viewBox="0 0 24 24"><path d="M6.6 10.8a15.1 15.1 0 0 0 6.6 6.6l2.2-2.2a1 1 0 0 1 1-.25 11.4 11.4 0 0 0 3.6.57 1 1 0 0 1 1 1V20a1 1 0 0 1-1 1A17 17 0 0 1 3 4a1 1 0 0 1 1-1h3.5a1 1 0 0 1 1 1c0 1.25.2 2.45.57 3.57a1 1 0 0 1-.25 1z" fill="#fff"/></svg></span><span>212-555-0176</span></div>
  <div class="f-contact abs" style="left:464px;top:236px"><span class="f-ico"><svg width="18" height="14" viewBox="0 0 18 14"><rect width="18" height="14" rx="1" fill="#fff"/><path d="M1 1l8 6 8-6" stroke="#333" stroke-width="1.5" fill="none"/></svg></span><span>info@tailbrook.com</span></div>
  <h3 class="f-head abs" style="left:772px;top:82px">Keep Updated</h3>
  <p class="abs" style="left:772px;top:116px;width:340px;font-size:15px;line-height:23px">Lorem ipsum dolor sit amet, cocr adipiscing elit, sed do eiusmod tempor incididunt ut</p>
  <div class="abs" style="left:770px;top:236px;display:flex;gap:9px">
    <span class="social" aria-label="Social link"><i></i></span>
    <span class="social" aria-label="Social link"><i></i></span>
    <span class="social" aria-label="Social link"><i></i></span>
    <span class="social" aria-label="Social link"><i></i></span>
  </div>
</footer>
<div class="email abs">Your Email</div>
<div class="send abs"><svg width="20" height="18" viewBox="0 0 20 18"><path d="M1 8L19 1l-4 16-5-5-3 4v-6l9-8-11 7z" fill="#fff"/></svg></div>
<div class="rule abs"></div>
<p class="copy abs" style="color:#fff">Copyright © 2021 Tailbrook. All rights reserved.</p>

</body>
</html>
```